Web Design Project

The Varnholt Group is a strategy consulting group that works primarily with the healthcare industry. We provide a limited range of strategic planning & marketing services designed to focus on the growth and future viability of our clients’ organizations. We are a very small organization, but want to communicate a sense of boldness, forward-looking/visionary, and both creative and analytic. What follows below is: 1) A simple overview of the outline of the web-pages; 2) an important list of web-sites that appeal to me – the most important of which appears in a larger font; 3) photo ideas for the home page (from Pictavo.com). I have not written copy…and won’t until I know length based upon design.

The Varnholt Group
Healthcare Strategic Consulting

(Key Sections for the site)
HOME PAGE ABOUT US SERVICES NEWS & COMMENTS CONTACT US

(Sites That I Admire:)

http://www.lumenwirk.eu/services/ Very creative use of iconography to represent services, etc.

http://quillmoss.com/ Arresting graphics

http://brontiva.co/ GREAT SITE. THIS IS THE SITE THAT I LIKE THE MOST IN TERMS OF GENERAL LOOK & FEEL.

http://kasperholm.com/ Very interesting, stark/bold B&W site for architects

http://www.rtmalvey.com/ Interesting home page for promoting individual

HOME PAGE:

The Varnholt Group
STRATEGIC CONSULTING SERVICES (should be bold). We have a Logo that can be supplied later

Pictavo Image Options: 47193652, 36840157, 29617483, 58302619, 274815936, 61948237
Updates

Project Deadline Extended
Reason: The 1st and 2nd place designers will have an additional 5-7 days to complete the remaining pages of the site (approximately 11 pages). I have a file with all the photo information and rough copy that can be dropped into position.

Target Market(s)

Senior Executives (CEO,COO, CFO,SVP) in major hospitals or healthcare systems, other senior executives within healthcare.

Industry/Entity Type

Healthcare

Requirements
Must have
• I will want to pay to have this project expanded to show look and feel for:
*Home Page and key sections
*4 Pages that will be under the "About Us" heading
*5 Pages that will be under the "Services" heading

I have image options selected from Pictavo for all key sections. We will need to look at the cost for those images that the designer recommends.

```html
<!DOCTYPE html>
<html lang="en">
<head>
<meta charset="utf-8">
<title>The Varnholt Group — Healthcare Strategic Consulting</title>
<link rel="stylesheet" href="https://fonts.googleapis.com/css2?family=Lato:wght@400;700&family=Montserrat:wght@600;700&family=Roboto+Condensed:wght@300&family=Arimo:wght@400;700&display=swap">
<style>
:root{
  --navy:#12103a;
  --gold-deep:#eea21a;
  --cream:#fffbe8;
  --panel:#3a3a3a;
  --panel-edge:#8a8a8a;
  --footer:#141414;
  --footer-text:#c9c9c9;
  --white:#ffffff;
}
*{margin:0;padding:0;box-sizing:border-box}
html,body{width:1200px;height:926px;overflow:hidden}
body{position:relative;font-family:"Arimo",sans-serif;color:var(--navy);
  background:radial-gradient(ellipse 620px 420px at 560px 290px,var(--cream) 0%,#fff6cf 35%,#fbd86a 65%,var(--gold-deep) 100%)}
.abs{position:absolute}
.brand{left:173px;top:22px}
.brand-name{font-family:"Lato",sans-serif;font-weight:700;font-size:30px;color:var(--navy);line-height:1}
.brand-tag{font-family:"Lato",sans-serif;font-weight:400;font-size:12px;letter-spacing:1px;color:var(--navy);margin-top:7px}
.header-line{left:172px;top:86px;width:830px;height:2px;background:linear-gradient(90deg,transparent,rgba(0,0,0,.12),transparent)}
.nav-tab{left:559px;top:0;width:64px;height:99px}
.nav{left:574px;top:53px;font-family:"Montserrat",sans-serif;font-weight:600;font-size:11px;color:var(--navy)}
.nav a{color:inherit;text-decoration:none;position:absolute;white-space:nowrap}
.nav .active{color:var(--white)}
.search{left:761px;top:15px;width:242px;height:22px;border-radius:5px;background:linear-gradient(#fff,#eee);border:1px solid #ccc;font-size:12px;color:#555;padding:3px 14px}
.search svg{position:absolute;right:8px;top:2px}
.hero-title{left:178px;font-family:"Lato",sans-serif;font-weight:700;font-size:47px;letter-spacing:-2px;line-height:1;white-space:nowrap}
.t1{top:160px;color:var(--navy)}
.band{left:174px;top:214px;width:330px;height:59px;background:var(--navy);clip-path:polygon(0 0,100% 0,96% 100%,0 100%)}
.t2{top:221px;color:#d9d9e2;font-weight:400}
.t3{top:287px;color:#111}
.intro{left:176px;top:352px;width:330px;font-family:"Lato",sans-serif;font-size:13px;line-height:18.6px;color:#1b1b40}
.art{left:497px;top:94px;width:566px;height:377px;background:radial-gradient(ellipse at 70% 75%,rgba(40,30,10,.45),rgba(255,250,230,0) 70%)}
.sec-title{top:480px;font-family:"Montserrat",sans-serif;font-weight:700;font-size:18px;letter-spacing:1.5px;color:var(--navy)}
.card{top:503px;width:202px;height:112px;background:var(--panel);border-bottom:4px solid var(--panel-edge);color:#f2f2f2;font-size:10.5px;letter-spacing:.6px;line-height:12.5px}
.card svg.icon{position:absolute;left:25px;top:32px}
.card p{position:absolute;left:87px;top:15px;width:110px}
.card.contact p{left:66px;width:134px;font-size:10px;letter-spacing:0;line-height:13.6px}
.card .pointer{position:absolute;right:-9px;top:47px;width:0;height:0;border-top:9px solid transparent;border-bottom:9px solid transparent;border-left:9px solid #fff7dd}
.footer{left:0;top:658px;width:1200px;height:268px;background:var(--footer)}
.f-title{top:670px;font-family:"Roboto Condensed",sans-serif;font-weight:300;font-size:20px;color:#d8d8d8}
.f-links{top:710px;list-style:none;font-size:11px;font-weight:700;color:var(--footer-text);line-height:19.5px}
.recommend{left:470px;top:721px;width:76px;height:20px;border:1px solid #888;border-radius:2px;background:linear-gradient(#ddd,#aaa);font-size:9.5px;color:#333;padding:4px 0 0 18px;white-space:nowrap}
.recommend span{position:absolute;left:5px;top:5px;width:9px;height:9px;border:1.5px solid #333}
.rec-mark{left:551px;top:722px;width:10px;height:10px;background:#4a64a8}
.rec-note{left:566px;top:722px;font-size:9.5px;color:#8a8a8a;line-height:12px;letter-spacing:.3px}
.social{left:843px;top:699px;width:150px;height:30px;border-radius:15px;background:#d6d6d6;display:flex;justify-content:space-around;align-items:center;padding:0 10px}
.social i{display:block;width:20px;height:20px;border-radius:50%;background:#6a6a6a}
.copy{left:846px;top:743px;width:148px;text-align:center;font-size:11px;line-height:16.5px;color:#e3e3e3}
.legal{font-size:10.5px;color:var(--footer-text);text-decoration:underline;white-space:nowrap}
.sep{font-size:11px;color:#ccc}
</style>
</head>
<body>
<header>
  <div class="abs brand">
    <div class="brand-name">The Varnholt Group</div>
    <div class="brand-tag">Healthcare Strategic Consulting</div>
  </div>
  <div class="abs header-line"></div>
  <svg class="abs nav-tab" viewBox="0 0 64 99"><polygon points="0,0 64,0 64,92 32,99 0,92" fill="#12103a"/></svg>
  <nav class="abs nav">
    <a class="active" style="left:0">HOME</a>
    <a style="left:58px">ABOUT US</a>
    <a style="left:136px">SERVICES</a>
    <a style="left:218px">NEWS &amp; COMMENTS</a>
    <a style="left:352px">CONTACT US</a>
  </nav>
  <div class="abs search">Search:
    <svg width="18" height="18" viewBox="0 0 18 18"><circle cx="11" cy="7" r="5" fill="none" stroke="#222" stroke-width="2"/><line x1="7.5" y1="10.5" x2="2" y2="16" stroke="#222" stroke-width="2.5"/></svg>
  </div>
</header>

<main>
  <div class="abs band"></div>
  <h1 class="abs hero-title t1">STRATEGIC</h1>
  <div class="abs hero-title t2">CONSULTING</div>
  <div class="abs hero-title t3">SERVICES</div>
  <p class="abs intro">Lorem ipsum dolor sit amet, consectetuer adipiscing elit, sed diam nonummy nibh euismod tincidunt ut laoreet dolore magna aliquam erat volutpat. Ut wisi enim ad minim veniam.</p>
  <div class="abs art" role="img" aria-label="Hand-drawn strategy diagram with two business people shaking hands in silhouette"></div>

  <h2 class="abs sec-title" style="left:173px">SOLUTIONS</h2>
  <h2 class="abs sec-title" style="left:383px">COMMENTS</h2>
  <h2 class="abs sec-title" style="left:595px">SERVICES</h2>
  <h2 class="abs sec-title" style="left:805px">CONTACT</h2>

  <div class="abs card" style="left:171px">
    <svg class="icon" width="46" height="46" viewBox="0 0 46 46" fill="none" stroke="#f3c85a" stroke-width="2.5"><circle cx="23" cy="23" r="20"/><circle cx="23" cy="23" r="13"/><circle cx="23" cy="23" r="6"/></svg>
    <p>Mam libero tempore massasoluta nobis est eligendi omnis volutassumenda est,omnis doloresed</p>
    <span class="pointer"></span>
  </div>
  <div class="abs card" style="left:381px">
    <svg class="icon" width="46" height="46" viewBox="0 0 46 46"><circle cx="23" cy="23" r="20" fill="none" stroke="#fff" stroke-width="2.5"/><circle cx="16" cy="18" r="3.5" fill="#fff"/><circle cx="29" cy="29" r="3.5" fill="#fff"/></svg>
    <p>Mam libero tempore sasoluta nobis est eligendi omnis volutasass umenda est,omnis dolresed</p>
    <span class="pointer"></span>
  </div>
  <div class="abs card" style="left:592px">
    <svg class="icon" width="46" height="46" viewBox="0 0 46 46" fill="none" stroke="#fff" stroke-width="2.5"><path d="M10 8 Q2 23 10 38"/><path d="M36 8 Q44 23 36 38"/><circle cx="23" cy="23" r="3.5" fill="#fff" stroke="none"/><polygon points="23,4 28,11 18,11" fill="#fff" stroke="none"/><rect x="21" y="11" width="4" height="5" fill="#fff" stroke="none"/><polygon points="23,42 28,35 18,35" fill="#fff" stroke="none"/><rect x="21" y="30" width="4" height="5" fill="#fff" stroke="none"/></svg>
    <p style="left:95px;width:104px">Mam libero tempore massasoluta nobis est eligendi omnis volutassumenda est,omnis dolores.</p>
    <span class="pointer"></span>
  </div>
  <div class="abs card contact" style="left:803px">
    <svg class="icon" style="left:14px" width="46" height="46" viewBox="0 0 46 46" fill="none" stroke="#fff" stroke-width="2.5"><circle cx="23" cy="23" r="20"/><path d="M10 15 L23 27 L36 15 M10 33 L19 24 M36 33 L27 24"/></svg>
    <p>4120 Aldermoor Place,<br>Brenfield, DC 45 Fr 45.<br>Support: +1 800 555 0142<br>Local: +1 800 555 0187<br>FAX: +1 504 555 0163<br>E-Mail: mail@varnholt.org</p>
  </div>
</main>

<footer>
  <div class="abs footer"></div>
  <h3 class="abs f-title" style="left:177px">THE VARNHOLT GROUP</h3>
  <ul class="abs f-links" style="left:177px"><li>Home</li><li>Benefits</li><li>About Us</li><li>Pricing &amp; Sign Up</li><li>Features</li><li>FAQs</li><li>Affiliate</li></ul>
  <ul class="abs f-links" style="left:321px"><li>Blog</li><li>API</li><li>Testimonials</li><li>Tour</li><li>Support</li><li>Contact Us</li><li>Invite Friends</li></ul>

  <h3 class="abs f-title" style="left:470px">LATEST TWEETS</h3>
  <div class="abs recommend"><span></span>Recommend</div>
  <div class="abs rec-mark"></div>
  <div class="abs rec-note">206 people<br>recommend this. Be</div>

  <h3 class="abs f-title" style="left:846px">JOIN US AT</h3>
  <div class="abs social"><i></i><i></i><i></i><i></i></div>
  <p class="abs copy">Copyright 2012 The Varnholt Group All Rights reserved.</p>
  <a class="abs legal" style="left:843px;top:792px">Privacy Policy</a><span class="abs sep" style="left:916px;top:791px">|</span><a class="abs legal" style="left:927px;top:792px">Terms Of Service</a>
  <a class="abs legal" style="left:843px;top:820px">Data Backup</a><span class="abs sep" style="left:916px;top:819px">|</span><a class="abs legal" style="left:927px;top:820px">Partnership</a>
  <a class="abs legal" style="left:895px;top:849px">Feedback</a>
</footer>
</body>
</html>
```